Brand new website for global research and investment startup

We need a simple website, maybe 3 pages: landing page with business description, investment philosophy, team and contact info.
We have a logo already that can be incorporated. Please use the logo only, not the text
We like the color green, something along the lines of #3D6C32 as the main color.
We'd like to design the website with geometric shapes in gradations of the base color. The shapes should suggest "work in progress", "built to last (a long time)", "solidity" and "indestructibility". One idea floating in my head sees smaller features with icosahedron and dodecahedron shapes, and maybe larger structures like crystal lattices; but please feel free to be creative and imagine your own.

```html
<!DOCTYPE html>
<html lang="en">
<head>
<meta charset="utf-8">
<title>Northfield Research — Research with Conviction</title>
<link rel="stylesheet" href="https://fonts.googleapis.com/css2?family=Rubik:wght@300;400;500;600;700&family=Nunito+Sans:wght@300;400;600&display=swap">
<style>
:root{
  --green-main:#3d6c32;
  --green-deep:#0f2a0d;
  --green-dark:#2b5a2e;
  --green-title:#2f5e2a;
  --green-bright:#4ea53d;
  --grey-bg:#f3f5f4;
  --ink:#1d1d1d;
  --text:#3a3a3a;
  --muted:#666;
  --white:#fff;
}
*{margin:0;padding:0;box-sizing:border-box}
html,body{width:1200px;height:3016px;overflow:hidden}
body{position:relative;background:var(--white);font-family:"Nunito Sans",sans-serif;color:var(--text)}
.abs{position:absolute}

/* hero */
.hero{position:absolute;left:0;top:0;width:1200px;height:731px;
  clip-path:polygon(0 0,100% 0,100% 646px,50% 731px,0 646px);
  background:linear-gradient(115deg,#0c200b 0%,#143a12 40%,#2a6324 75%,#5a9a4e 100%)}
.hero-art{position:absolute;left:560px;top:80px;width:640px;height:600px;
  background:radial-gradient(ellipse at 60% 45%,rgba(150,210,130,.45) 0%,rgba(90,160,80,.2) 40%,rgba(0,0,0,0) 70%)}
.brand{position:absolute;left:130px;top:44px;font-family:"Rubik",sans-serif;font-weight:600;font-size:28px;color:var(--white);display:flex;align-items:center;gap:10px}
.brand-dot{width:14px;height:14px;border-radius:50%;background:var(--white)}
.nav{position:absolute;top:52px;left:401px;display:flex;gap:26px;font-family:"Rubik",sans-serif;font-size:14.5px;font-weight:500;color:var(--white)}
.nav .active{color:var(--green-bright);text-decoration:underline;text-underline-offset:4px}
.btn-outline{position:absolute;left:942px;top:42px;width:128px;height:40px;border:1px solid rgba(255,255,255,.8);color:var(--white);font-family:"Rubik",sans-serif;font-size:12.5px;font-weight:500;display:flex;align-items:center;justify-content:center}
.hero-title{position:absolute;left:130px;top:236px;font-family:"Rubik",sans-serif;font-weight:300;font-size:46px;line-height:52px;color:var(--white);text-transform:uppercase}
.hero-title b{font-weight:700}
.hero-lead{position:absolute;left:130px;top:402px;width:560px;font-size:20px;line-height:28px;color:#eef3ee;font-weight:300}
.btn{display:flex;align-items:center;justify-content:center;gap:10px;background:var(--green-main);color:var(--white);font-family:"Rubik",sans-serif;font-size:12.5px;font-weight:500;text-transform:uppercase}
.btn svg{width:16px;height:10px}

/* who */
.center{left:0;width:1200px;text-align:center}
.sec-title{font-family:"Rubik",sans-serif;font-weight:600;font-size:36px;color:var(--green-title)}
.sec-sub{font-family:"Rubik",sans-serif;font-weight:500;font-size:21px;color:var(--ink)}
.para{font-size:18px;line-height:24px;color:var(--text);font-weight:300}
.card{position:absolute;top:1089px;width:293px;height:232px;background:var(--white);border:1px solid #e2e2e2;box-shadow:0 2px 4px rgba(0,0,0,.08);text-align:center}
.card h3{position:absolute;top:88px;left:0;width:100%;font-family:"Rubik",sans-serif;font-weight:500;font-size:15.5px;color:var(--green-title)}
.card p{position:absolute;top:118px;left:30px;right:30px;font-size:11px;line-height:17px;color:var(--muted)}
.hex{position:absolute;top:1030px;width:116px;height:132px}

/* approach */
.approach{position:absolute;left:0;top:1424px;width:1200px;height:761px;background:var(--grey-bg);
  clip-path:polygon(0 81px,50% 0,100% 81px,100% 671px,50% 761px,0 671px)}
.eyebrow{font-family:"Rubik",sans-serif;font-size:18px;color:var(--green-title)}
.ap-title{font-family:"Rubik",sans-serif;font-weight:600;font-size:25px;line-height:33px;color:var(--ink)}
.rule{background:var(--green-bright);height:2px;width:160px}
.list{list-style:none;font-size:15.5px;color:var(--text)}
.list li{height:27px;position:relative;padding-left:29px}
.list li::before{content:"";position:absolute;left:0;top:9px;width:3px;height:3px;border-radius:50%;background:var(--green-main)}
.photo{position:absolute;border:2px solid var(--white);box-shadow:0 2px 6px rgba(0,0,0,.15)}

/* contact */
.contact-bg{position:absolute;left:0;top:2100px;width:1200px;height:520px;
  background:radial-gradient(ellipse at 85% 30%,rgba(200,205,200,.35),rgba(255,255,255,0) 60%),radial-gradient(ellipse at 15% 80%,rgba(200,205,200,.3),rgba(255,255,255,0) 55%)}

/* footer */
.footer{position:absolute;left:0;top:2533px;width:1200px;height:483px;background:var(--green-dark);
  clip-path:polygon(0 80px,50% 0,100% 80px,100% 100%,0 100%)}
.f-brand{position:absolute;left:130px;top:2748px;font-family:"Rubik",sans-serif;font-weight:600;font-size:30px;color:var(--white);display:flex;align-items:center;gap:10px}
.f-head{position:absolute;top:2680px;font-family:"Rubik",sans-serif;font-weight:500;font-size:14px;color:var(--white)}
.f-text{position:absolute;font-size:11px;line-height:15.5px;color:#e4ece3}
.input{position:absolute;left:369px;top:2783px;width:190px;height:35px;background:var(--white);font-family:"Rubik",sans-serif;font-size:11px;color:var(--ink);padding:12px 16px}
.subscribe{position:absolute;left:559px;top:2783px;width:134px;height:35px;background:var(--green-bright);color:var(--white);font-family:"Rubik",sans-serif;font-size:12px;font-weight:500;display:flex;align-items:center;justify-content:center}
.social{position:absolute;top:2845px;width:24px;height:24px;border:1.5px solid rgba(255,255,255,.8);border-radius:50%}
.f-link{position:absolute;left:972px;font-size:11.5px;color:#e4ece3}
.f-rule{position:absolute;left:130px;top:2916px;width:940px;height:1px;background:rgba(255,255,255,.18)}
.copy{position:absolute;top:2956px;left:0;width:1200px;text-align:center;font-size:15px;color:#e4ece3}
</style>
</head>
<body>

<section class="hero">
  <div class="hero-art" role="img" aria-label="Glowing green wireframe polyhedra connected by a network of points and lines"></div>
</section>
<div class="brand"><span class="brand-dot"></span>Northfield</div>
<nav class="nav">
  <span class="active">HOME</span><span>INVESTMENT PHILOSOPHY</span><span>INSIGHTS</span><span>MEET OUR TEAM</span>
</nav>
<div class="btn-outline">GET IN TOUCH</div>
<h1 class="hero-title">Research with<br>conviction. <b>Investing</b><br><b>with purpose.</b></h1>
<p class="hero-lead">Independent research and disciplined investment thinking for professional investors seeking long-term opportunity.</p>
<div class="btn abs" style="left:130px;top:480px;width:233px;height:39px">Explore our philosophy
  <svg viewBox="0 0 16 10"><path d="M0 5h14M10 1l4 4-4 4" fill="none" stroke="#fff" stroke-width="1.5"/></svg></div>

<h2 class="sec-title abs center" style="top:834px">WHO WE ARE</h2>
<p class="sec-sub abs center" style="top:892px">INDEPENDENT THINKING FOR A CHANGING MARKET.</p>
<p class="para abs" style="left:190px;width:820px;top:935px;text-align:center">We are a global research and investment firm focused on uncovering compelling opportunities in equity markets. Our approach is built on deep fundamental research, independent thinking and a long-term perspective.</p>

<div class="card" style="left:130px"><h3>Independent Research</h3><p>Lorem ipsum dolor sit amet, consectetur adipiscing elit, sed do eiusmod tempor incididunt ut labore et dolore magna aliqua. Ut enim ad minim veniam, quis nostrud exercitation ullamcoea.</p></div>
<div class="card" style="left:453px"><h3>Global Perspective</h3><p>Lorem ipsum dolor sit amet, consectetur adipiscing elit, sed do eiusmod tempor incididunt ut labore et dolore magna aliqua. Ut enim ad minim veniam, quis nostrud exercitation ullamcoea.</p></div>
<div class="card" style="left:777px"><h3>Long-Term Focus</h3><p>Lorem ipsum dolor sit amet, consectetur adipiscing elit, sed do eiusmod tempor incididunt ut labore et dolore magna aliqua. Ut enim ad minim veniam, quis nostrud exercitation ullamcoea.</p></div>

<svg class="hex" style="left:218px" viewBox="0 0 116 132"><polygon points="58,4 112,34 112,98 58,128 4,98 4,34" fill="#fff" stroke="#4ea53d" stroke-width="7"/>
  <g fill="none" stroke="#4ea53d" stroke-width="2"><circle cx="55" cy="52" r="11"/><path d="M48 70l-8 8M35 92h50M40 92v-10M50 92v-16M60 92v-12M70 92v-20M80 92v-26"/><path d="M50 52l4 4 7-7"/></g></svg>
<svg class="hex" style="left:541px" viewBox="0 0 116 132"><polygon points="58,4 112,34 112,98 58,128 4,98 4,34" fill="#fff" stroke="#4ea53d" stroke-width="7"/>
  <g fill="none" stroke="#4ea53d" stroke-width="2"><circle cx="48" cy="66" r="15"/><path d="M33 66h30M48 51c-6 8-6 22 0 30M48 51c6 8 6 22 0 30"/><circle cx="68" cy="80" r="9"/><path d="M74 86l7 7"/><path d="M62 48c4-4 12-4 16 0c-4 4-12 4-16 0z"/></g></svg>
<svg class="hex" style="left:865px" viewBox="0 0 116 132"><polygon points="58,4 112,34 112,98 58,128 4,98 4,34" fill="#fff" stroke="#4ea53d" stroke-width="7"/>
  <g fill="none" stroke="#4ea53d" stroke-width="2"><rect x="38" y="40" width="30" height="34"/><path d="M43 66v-8M50 66v-14M57 66v-10M68 50l14-10M76 40h6v6"/><rect x="32" y="78" width="26" height="16"/><path d="M37 83h4M45 83h4M37 89h4M45 89h4"/><circle cx="72" cy="86" r="9"/><path d="M72 81v5h4"/></g></svg>

<section class="approach"></section>
<p class="eyebrow abs" style="left:130px;top:1597px">OUR APPROACH</p>
<h2 class="ap-title abs" style="left:130px;top:1624px">A DISCIPLINED<br>APPROACH TO FINDING<br>WHAT OTHERS OVERLOOK.</h2>
<div class="rule abs" style="left:130px;top:1728px"></div>
<ul class="list abs" style="left:130px;top:1757px">
  <li>Invest with founders</li><li>Exceptional businesses</li><li>Participate in long-term success</li><li>Valuation-sensitive</li><li>Conviction-sizing of positions</li><li>Diversify across sectors and value drivers</li><li>UCITS compliant</li>
</ul>
<div class="btn abs" style="left:130px;top:1969px;width:140px;height:37px">Learn more
  <svg viewBox="0 0 16 10"><path d="M0 5h14M10 1l4 4-4 4" fill="none" stroke="#fff" stroke-width="1.5"/></svg></div>
<svg class="abs" style="left:522px;top:1632px" width="96" height="156"><path d="M1 155V1h95" fill="none" stroke="#4ea53d" stroke-width="2"/></svg>
<div class="photo" style="left:615px;top:1575px;width:454px;height:360px;background:linear-gradient(120deg,#6f7371 0%,#9a9e9c 55%,#c9cbc8 100%)" role="img" aria-label="Hand watering a small potted plant shaped like a rising arrow chart"></div>
<div class="photo" style="left:498px;top:1785px;width:397px;height:248px;background:linear-gradient(135deg,#3f6e36 0%,#1f4a1c 50%,#0f2c0d 100%)" role="img" aria-label="Green stock market candlestick chart"></div>

<div class="contact-bg" role="img" aria-label="Faint grey hexagonal lattice background"></div>
<h2 class="sec-title abs center" style="top:2284px">LET’S START A CONVERSATION</h2>
<p class="para abs" style="left:190px;width:820px;top:2340px;text-align:center">For professional investors interested in learning more about our research and investment approach, we welcome the opportunity to connect.</p>
<div class="btn abs" style="left:531px;top:2411px;width:139px;height:37px">Contact us
  <svg viewBox="0 0 16 10"><path d="M0 5h14M10 1l4 4-4 4" fill="none" stroke="#fff" stroke-width="1.5"/></svg></div>

<footer class="footer"></footer>
<div class="f-brand"><span class="brand-dot"></span>Northfield</div>
<p class="f-head" style="left:369px">SUBSCRIBE TO OUR MAILING LIST</p>
<p class="f-text" style="left:369px;top:2716px;width:300px">Sed ut perspiciatis unde omnis iste natus voluptatem accusantium doloremque laudantium, totam rem ariam, eaque ipsa quae ab illo inventore</p>
<div class="input">Email</div>
<div class="subscribe">SUBSCRIBE</div>
<span class="social" style="left:371px"></span><span class="social" style="left:404px"></span><span class="social" style="left:438px"></span><span class="social" style="left:471px"></span><span class="social" style="left:504px"></span>

<p class="f-head" style="left:738px">CONTACT US</p>
<svg class="abs" style="left:741px;top:2728px" width="10" height="14"><path d="M5 13C1 8 1 6 1 5a4 4 0 018 0c0 1 0 3-4 8z" fill="none" stroke="#4ea53d" stroke-width="1.2"/><circle cx="5" cy="5" r="1.5" fill="#4ea53d"/></svg>
<p class="f-text" style="left:764px;top:2720px;width:180px">2140 Meridian Ave, Suite 300,<br>United States</p>
<svg class="abs" style="left:740px;top:2770px" width="12" height="12"><path d="M2 1l3 0 1 3-2 1c1 2 2 3 4 4l1-2 3 1 0 3c-6 0-10-4-10-10z" fill="none" stroke="#4ea53d" stroke-width="1.1"/></svg>
<p class="f-text" style="left:764px;top:2768px">+1 (555) 014 2290</p>
<svg class="abs" style="left:740px;top:2801px" width="13" height="10"><rect x=".5" y=".5" width="12" height="9" fill="none" stroke="#4ea53d"/><path d="M.5 .5l6 5 6-5" fill="none" stroke="#4ea53d"/></svg>
<p class="f-text" style="left:764px;top:2799px">info@northfieldresearch.com</p>

<p class="f-head" style="left:972px">QUICK LINKS</p>
<p class="f-link" style="top:2717px">Home</p>
<p class="f-link" style="top:2744px">Investment Philosophy</p>
<p class="f-link" style="top:2771px">Insights</p>
<p class="f-link" style="top:2798px">Meet Our Team</p>
<p class="f-link" style="top:2825px">Contact Us</p>
<div class="f-rule"></div>
<p class="copy">© 2026 &nbsp;| &nbsp;All Rights Reserved</p>

</body>
</html>
```